Thistle Cafe's Web Page
Thank you for all the hardwork. Happy to see there are so many beautiful artworks. We have tried very hard to select the final winner. All the best in the year of Rabbit!!
We will post more contest later.Just stay tune!!
Good luck for all!!
good luck tremiko !!!
kindly rate template
thank you.
Can you kindly Rate our templates.
so that we will able to guess our work judgment.. how much effort we need more to create exact design!!!
Hi Guys! The reason I justified the work of Quillaro work is the outline of the web page not the software itself. When I look at the designs and the tones are mostly in black color and I think you will do the same thing as me. Do you all agree??
Corvel! your artwork is quite interesting too! Especially the slogan you made!! Your design is one of our consideration too!!
well i am waiting for your feedback. thanks
this whole thing is turning to a joke. enjoy
@ SirPlonk, Are you serious? You are only seeing part of my design. Please do not judge. Your comment is very offensive and you are belittling my work.
you're not serious are you ?
I think the design made by Quillarowork is quite attractive.
pomlet42 > Please let us know which designs you like so far. regards
Please check the design and rate :)
Best wishes
Wow! Quillarowork's design is quite nice. What's in the photo? Looks good!!
I found a website is quite interesting - http://www.brasvelo.com.au/. The designs that I recieved are similar. I hope the black color is not the only choice for us. Keep it going! Guys.Overall, the layouts are OK.
Just to verify, you will have both a set menu and a daily specials menu, is that correct. What other pages where you looking for on your site?
We are still renovating. It will be a good idea to spare some space for our cafe and our menu and special. We will be listen to any good suggestion!!
Logo has been uploaded
Thanks a lot :) I'M IN :)
Hi PH, Can you upload your logo so we know where to start? Thanks
We have a logo designed. It may be helpful to get some ideas. Please ask for it or browse the past projects (around late December) if needed.

```html
<!DOCTYPE html>
<html lang="en">
<head>
<meta charset="utf-8">
<title>Thistle Cafe</title>
<link rel="stylesheet" href="https://fonts.googleapis.com/css2?family=Noto+Sans:wght@400;700&display=swap">
<style>
  :root {
    --sidebar-bg: #1b0709;
    --gutter: #2d2a2a;
    --nav-bg: #d3602d;
    --nav-text: #fbe9dc;
    --nav-active: #ffffff;
    --brand-text: #f3e6dc;
    --brand-accent: #e0632c;
    --rule: #2a0e08;
  }
  * { margin: 0; padding: 0; box-sizing: border-box; }
  html, body { width: 1200px; height: 1002px; overflow: hidden; background: var(--gutter); }
  body { font-family: "Noto Sans", Verdana, sans-serif; }
  .page { position: relative; width: 1200px; height: 1002px; background: var(--gutter); }

  .sidebar {
    position: absolute; left: 0; top: 8px; width: 360px; height: 994px;
    background: var(--sidebar-bg);
  }
  .brand { position: absolute; left: 30px; top: 38px; }
  .brand-name {
    display: flex; align-items: center; gap: 12px;
    font-size: 66px; font-weight: 400; color: var(--brand-text);
    letter-spacing: 1px; line-height: 1;
  }
  .brand-dot { width: 16px; height: 16px; border-radius: 50%; background: var(--brand-accent); }
  .brand-tagline {
    margin: 6px 0 0 64px; font-size: 14px; color: var(--brand-accent);
    letter-spacing: 1px;
  }

  .nav-column {
    position: absolute; left: 376px; top: 8px; width: 210px; height: 994px;
    background: var(--nav-bg);
  }
  .main-nav { list-style: none; text-align: center; padding-top: 116px; }
  .main-nav li { font-size: 19px; color: var(--nav-text); height: 46px; line-height: 40px; }
  .main-nav li.is-current { color: var(--nav-active); font-weight: 700; }
  .main-nav li.divider { height: 14px; margin: -4px 20px 6px; border-top: 3px dashed var(--rule); }

  .slider-control {
    position: absolute; left: 12px; top: 476px; width: 186px;
    display: flex; align-items: center; gap: 6px;
    font-size: 14px; color: var(--nav-text);
  }
  .slider-track { flex: 1; height: 14px; }

  .hero-photo {
    position: absolute; left: 601px; top: 8px; width: 599px; height: 994px;
    background:
      radial-gradient(ellipse at 60% 55%, #e7c53a 0%, rgba(231,197,58,0.6) 18%, transparent 42%),
      radial-gradient(ellipse at 30% 10%, #e5542a 0%, transparent 30%),
      radial-gradient(ellipse at 20% 70%, #5a2414 0%, transparent 50%),
      linear-gradient(160deg, #7a4a30 0%, #4a2214 45%, #6b3a22 70%, #3a1a0e 100%);
  }
</style>
</head>
<body>
<div class="page">
  <aside class="sidebar">
    <div class="brand">
      <div class="brand-name"><span class="brand-dot"></span>Thistle</div>
      <div class="brand-tagline">modern asian cuisine</div>
    </div>
  </aside>

  <nav class="nav-column">
    <ul class="main-nav">
      <li class="is-current">home</li>
      <li>about</li>
      <li>menu</li>
      <li>gallery</li>
      <li>events</li>
      <li class="divider"></li>
      <li>contact</li>
    </ul>
    <div class="slider-control">
      <span>&lt;&lt;</span>
      <svg class="slider-track" viewBox="0 0 140 14" preserveAspectRatio="none">
        <line x1="0" y1="10" x2="140" y2="10" stroke="#2a0e08" stroke-width="3" stroke-dasharray="3 3"/>
        <rect x="8" y="0" width="3" height="14" fill="#2a0e08"/>
      </svg>
      <span>&gt;&gt;</span>
    </div>
  </nav>

  <div class="hero-photo" role="img" aria-label="Close-up photo of a grilled meat dish garnished with shredded yellow mango and red chilli"></div>
</div>
</body>
</html>
```